Security doors and flyscreens

We need business cards for our company called K & M Distributors. We quote, manufacture and install security doors and flyscreens.

Industry/Entity Type

Security

Contact Information for Business Card

K & M DISTRIBUTORS
17 Larkvale Rd. Ravenbrook 3081
Ph: 8157 2604
Fax: 8157 2609
Gavin: 0419 275 916
Email: gatesupplier@mailbox-example.net

```html
<!DOCTYPE html>
<html lang="en">
<head>
<meta charset="utf-8">
<title>K &amp; M Distributors — Business Card</title>
<link rel="stylesheet" href="https://fonts.googleapis.com/css2?family=Open+Sans:wght@400;600&display=swap">
<style>
  :root {
    --teal: #3bbfcd;
    --charcoal: #333333;
    --yellow: #f7dc0b;
    --paper: #efefef;
    --white: #ffffff;
    --backdrop: #d9d9d9;
  }
  html, body {
    margin: 0;
    width: 1200px;
    height: 1000px;
    overflow: hidden;
    background: var(--backdrop);
    font-family: "Open Sans", Arial, sans-serif;
  }
  .card {
    position: absolute;
    left: 150px;
    top: 240px;
    width: 900px;
    height: 520px;
    background: var(--charcoal);
    overflow: hidden;
    box-shadow: 0 6px 24px rgba(0,0,0,0.25);
  }
  .card__top {
    position: absolute;
    left: 0; top: 0;
    width: 900px; height: 200px;
    background: var(--teal);
  }
  .card__stripe {
    position: absolute;
    left: 0; top: 440px;
    width: 900px; height: 16px;
    background: var(--teal);
  }
  .card__base {
    position: absolute;
    left: 0; top: 456px;
    width: 900px; height: 64px;
    background: var(--paper);
  }
  .brand {
    position: absolute;
    left: 70px;
    top: 128px;
    margin: 0;
    font-size: 34px;
    font-weight: 400;
    letter-spacing: 1px;
    color: var(--charcoal);
  }
  .tagline {
    position: absolute;
    right: 60px;
    top: 112px;
    margin: 0;
    text-align: right;
    font-size: 23px;
    line-height: 1.15;
    font-weight: 400;
    color: var(--white);
  }
  .contacts {
    position: absolute;
    left: 80px;
    top: 228px;
    margin: 0;
    padding: 0;
    list-style: none;
    color: var(--white);
    font-size: 17px;
    line-height: 1.3;
  }
  .contacts__item {
    display: flex;
    align-items: center;
    gap: 14px;
    margin-bottom: 16px;
  }
  .contacts__icon {
    width: 32px;
    height: 32px;
    flex: none;
  }
  .person {
    position: absolute;
    left: 520px;
    top: 232px;
    color: var(--yellow);
    text-align: center;
  }
  .person__name {
    margin: 0;
    font-size: 44px;
    font-weight: 400;
    line-height: 1.1;
  }
  .person__phone {
    margin: 0;
    font-size: 38px;
    font-weight: 400;
    line-height: 1.15;
  }
</style>
</head>
<body>
  <article class="card">
    <div class="card__top"></div>
    <div class="card__stripe"></div>
    <div class="card__base"></div>

    <h1 class="brand">K &amp; M DISTRIBUTORS</h1>
    <p class="tagline">MANUFACTURE AND INSTALL<br>SECURITY DOORS AND FLYSCREENS</p>

    <ul class="contacts">
      <li class="contacts__item">
        <svg class="contacts__icon" viewBox="0 0 32 32" aria-hidden="true">
          <path d="M3 12c0-4 6-6 13-6s13 2 13 6v2h-6v-3H9v3H3z" fill="var(--yellow)"/>
          <path d="M8 15h16l4 12H4z" fill="var(--yellow)"/>
          <circle cx="16" cy="21" r="3.5" fill="var(--charcoal)"/>
        </svg>
        <span>8157 2604<br>8157 2609 (FAX)</span>
      </li>
      <li class="contacts__item">
        <svg class="contacts__icon" viewBox="0 0 32 32" aria-hidden="true">
          <g fill="none" stroke="var(--yellow)" stroke-width="2.2">
            <circle cx="16" cy="16" r="13"/>
            <ellipse cx="16" cy="16" rx="6" ry="13"/>
            <line x1="3" y1="16" x2="29" y2="16"/>
            <line x1="16" y1="3" x2="16" y2="29"/>
            <path d="M5.5 9h21M5.5 23h21"/>
          </g>
        </svg>
        <span>gatesupplier@mailbox-example.net</span>
      </li>
      <li class="contacts__item">
        <svg class="contacts__icon" viewBox="0 0 32 32" aria-hidden="true">
          <polygon points="16,3 30,16 26,16 26,29 6,29 6,16 2,16" fill="var(--yellow)"/>
          <rect x="13" y="19" width="6" height="10" fill="var(--charcoal)"/>
        </svg>
        <span>17 Larkvale Rd.<br>Ravenbrook 3081</span>
      </li>
    </ul>

    <div class="person">
      <p class="person__name">GAVIN</p>
      <p class="person__phone">0419 275 916</p>
    </div>
  </article>
</body>
</html>
```